Industrial Inspection & Testing Company Needs Brochure

We need a brochure design for a company based in Western Pennsylvania, USA. Our company performs services mainly in industrial sites. These can include manufacturing, health & medical, power generation, and more. We use infrared thermography, vibration analysis, ultrasonic thickness testing, dynamic balancing and other practices to provide predictive maintenance to our customers. Please see our website for a more thorough explanation of our services. www.korbalinspect.com

Complete list of services:

Infrared Thermal Imaging
Vibration Analysis
High Temperature Video & Photography
High Speed Video
Laser Alignment
Dynamic Balancing
Motor Meggering
Leak Detection
Ultrasonic Thickness Testing
Oil Analysis

KTR, LLC - P.O. Box 4837 - Maplewick Township, PA 16239
Phone: 724-583-1149 / Fax: 724-583-1157

MISSION

KTR, LLC will provide the highest quality, cost effective, world class PdM services in the industry. Our commitment to continuing education and growth will afford our engineers the tools needed to stay on the cutting edge of technology. We believe in the implementation of Predictive Maintenance services to increase overall equipment reliability, reduce costs and improve profitability. Our goal is to provide continuous improvements to these processes. The company will network with various industry professionals to offer the widest range of equipment, training and reliability services available. Meeting these goals will ensure the company’s longevity and allow our valued customers to achieve the cost reduction goals that are needed in today’s competitive marketplace.
HISTORY
KTR, LLC was founded in March 1984, which emerged from the Greyhollow Alloy Works’ Development Laboratory, Monroeville, Pennsylvania. Its founders headed the Thermography and Photoinstrumentation Department of that facility.
While at the G. A. Works Development Laboratory, they established the utilization of thermography as a valuable tool for evaluating equipment and facilities in the steel industry. Their work set the standards for the use of thermography in the steel industry that continues today with KTR. Although the original thermographic equipment was crude, bulky and slow, KTR has maintained its position as an industry leader. Today KTR uses the most technologically advanced infrared systems available for on-site nondestructive industrial inspections.
In addition, while at G. A. Works Development, the founders of KTR pioneered the use of photographic cameras and high-speed motion pictures as another form of a predictive and preventative maintenance tool. Specially constructed camera systems with thermal protective housings were developed for inspecting blast furnace interior stockline armor areas, stove domes, and other high-temperature areas.
Today KTR remains on the cutting-edge in providing a wide range of nondestructive inspection services to industry.

***All of the photos and documents attached were either shot by us or purchased stock photos***

I realize that only a few images might be used, I just wanted to upload many to give designers a broad range to choose from.

Target Market(s)

Large industrial customers who use large amounts of electricity, heavy duty machinery, or both.

Industry/Entity Type

Industrial

Requirements
Must have
• Need a 3 full page tri-fold design (not skinny column tri-fold)

Contact information for our company, list of our services, our logo (possible redesign of logo), photos from our inspections that will be attached.
Nice to have
• List of services, breif explanation of each with graphical representation, contact information

```html
<!DOCTYPE html>
<html lang="en">
<head>
<meta charset="utf-8">
<title>KTR, LLC – Tri-fold Brochure</title>
<link rel="stylesheet" href="https://fonts.googleapis.com/css2?family=Arimo:wght@400;700&display=swap">
<style>
  :root {
    --orange: #f26a21;
    --orange-light: #f7941d;
    --charcoal: #1c1c1c;
    --steel: #3a3a3a;
    --steel-light: #5a5a5a;
    --white: #ffffff;
    --navy: #2e3a97;
    --text-light: #e9e9e9;
  }
  * { box-sizing: border-box; margin: 0; padding: 0; }
  html, body {
    width: 1200px; height: 915px; overflow: hidden;
    background: var(--charcoal);
    font-family: "Arimo", Arial, sans-serif;
  }
  .brochure { position: relative; width: 1200px; height: 915px; }
  .panel { position: absolute; top: 0; height: 915px; overflow: hidden; }
  .panel-bg { position: absolute; inset: 0; width: 100%; height: 100%; }

  /* About panel */
  .panel-about { left: 0; width: 401px; }
  .about-heading {
    position: absolute; top: 32px; left: 0; width: 401px; height: 32px;
    background: linear-gradient(90deg, #151515 0%, #3d3d3d 60%, #8a8a8a 100%);
    color: var(--white); font-size: 24px; line-height: 32px; padding-left: 30px;
  }
  .about-copy {
    position: absolute; top: 102px; left: 27px; width: 347px;
    color: var(--white); font-size: 12.6px; line-height: 17.4px; text-align: justify;
  }

  /* Services panel */
  .panel-services { left: 401px; width: 395px; }
  .services-title {
    position: absolute; top: 150px; left: 0; width: 395px; height: 21px;
    background: linear-gradient(90deg, rgba(90,90,90,0) 0%, #5e5e5e 30%, #5e5e5e 70%, rgba(90,90,90,0) 100%);
    color: var(--white); font-size: 11.5px; line-height: 21px; text-align: center;
  }
  .services-list {
    position: absolute; top: 180px; left: 0; width: 395px; list-style: none;
    color: var(--text-light); font-size: 13.5px; line-height: 26px; text-align: center;
  }
  .contact {
    position: absolute; top: 660px; left: 0; width: 395px; text-align: center; color: var(--white);
  }
  .brand-mark { font-size: 44px; font-weight: 700; color: var(--navy); letter-spacing: 1px; line-height: 58px; }
  .contact-name { font-size: 21px; line-height: 24px; }
  .contact-address { font-size: 11.5px; line-height: 14.5px; }
  .contact-lines { margin-top: 13px; font-size: 11.5px; line-height: 15px; }
  .contact-lines .label { color: var(--orange-light); }
  .web-pill {
    display: inline-block; margin-top: 24px; width: 172px; height: 17px;
    background: var(--orange-light); border-radius: 9px;
    color: var(--white); font-size: 14px; line-height: 17px;
  }

  /* Cover panel */
  .panel-cover { left: 796px; width: 404px; }
  .cover-brand {
    position: absolute; top: 92px; left: 70px; width: 220px; text-align: center;
    font-size: 72px; font-weight: 700; color: var(--navy); letter-spacing: 2px;
  }
</style>
</head>
<body>
<main class="brochure">

  <section class="panel panel-about">
    <svg class="panel-bg" viewBox="0 0 401 915" preserveAspectRatio="none" aria-hidden="true">
      <defs>
        <linearGradient id="aboutOrange" x1="0" y1="0" x2="1" y2="1">
          <stop offset="0" stop-color="#f7941d"/>
          <stop offset="0.55" stop-color="#f26a21"/>
          <stop offset="1" stop-color="#e4561c"/>
        </linearGradient>
        <linearGradient id="brushedDark" x1="0" y1="0" x2="1" y2="0">
          <stop offset="0" stop-color="#2e2e2e"/>
          <stop offset="0.5" stop-color="#4a4a4a"/>
          <stop offset="1" stop-color="#2a2a2a"/>
        </linearGradient>
      </defs>
      <rect width="401" height="915" fill="url(#brushedDark)"/>
      <polygon points="0,0 401,0 401,556 0,615" fill="url(#aboutOrange)"/>
      <polygon points="0,615 401,556 401,582 0,630" fill="#151515"/>
    </svg>
    <svg class="panel-bg" viewBox="0 0 401 915" preserveAspectRatio="none" role="img" aria-label="Photo of an oil refinery silhouetted at sunset, lights reflected in the water">
      <defs>
        <linearGradient id="refinerySunset" x1="0" y1="0" x2="0" y2="1">
          <stop offset="0" stop-color="#3a2440"/>
          <stop offset="0.35" stop-color="#c43a4a"/>
          <stop offset="0.55" stop-color="#1a1418"/>
          <stop offset="0.75" stop-color="#d2303c"/>
          <stop offset="1" stop-color="#3a1018"/>
        </linearGradient>
      </defs>
      <polygon points="0,630 401,582 401,872 0,795" fill="url(#refinerySunset)"/>
    </svg>
    <h2 class="about-heading">ABOUT US</h2>
    <div class="about-copy">
      <p>KTR, LLC was founded in March 1984, which emerged from the Greyhollow Alloy Works’ Development Laboratory, Monroeville, Pennsylvania. Its founders headed the Thermography and Photo instrumentation Department of that facility.</p>
      <p>While at the G. A. Works Development Laboratory, they established the utilization of thermography as a valuable tool for evaluating equipment and facilities in the steel industry. Their work set the standards for the use of thermography in the steel industry that continues today with KTR. Although the original thermographic equipment was crude, bulky and slow, KTR has maintained its position as an industry leader. Today KTR uses the most technologically advanced infrared systems available for on-site nondestructive industrial inspections.</p>
      <p>In addition, while at G. A. Works Development, the founders of KTR pioneered the use of photographic cameras and high-speed motion pictures as another form of a predictive and preventative maintenance tool. Specially constructed camera systems with thermal protective housings were developed for inspecting blast furnace interior stockline armor areas, stove domes, and other high-temperature areas.</p>
      <p>Today KTR remains on the cutting-edge in providing a wide range of nondestructive inspection services to industry.</p>
    </div>
  </section>

  <section class="panel panel-services">
    <svg class="panel-bg" viewBox="0 0 395 915" preserveAspectRatio="none" aria-hidden="true">
      <defs>
        <linearGradient id="servicesDark" x1="0" y1="0" x2="0" y2="1">
          <stop offset="0" stop-color="#0e0e0e"/>
          <stop offset="0.55" stop-color="#1e1e1e"/>
          <stop offset="1" stop-color="#3a3a3a"/>
        </linearGradient>
      </defs>
      <rect width="395" height="915" fill="url(#servicesDark)"/>
      <rect width="395" height="14" fill="#4a4a4a"/>
    </svg>
    <h2 class="services-title">Complete list of services</h2>
    <ul class="services-list">
      <li>Infrared Thermal Imaging</li>
      <li>Vibration Analysis</li>
      <li>High Temperature Video &amp; Photography</li>
      <li>High Speed Video</li>
      <li>Laser Alignment</li>
      <li>Dynamic Balancing</li>
      <li>Motor Meggering</li>
      <li>Leak Detection</li>
      <li>Ultrasonic Thickness Testing</li>
      <li>Oil Analysis</li>
    </ul>
    <address class="contact" style="font-style:normal">
      <div class="brand-mark">KTR</div>
      <div class="contact-name">KTR, LLC</div>
      <div class="contact-address">P.O. Box 4837<br>Maplewick Township, PA 16239</div>
      <div class="contact-lines">
        <span class="label">Phone:</span> 724-583-1149<br>
        <span class="label">Fax:</span> 724-583-1157
      </div>
      <div class="web-pill">www.korbalinspect.com</div>
    </address>
  </section>

  <section class="panel panel-cover">
    <svg class="panel-bg" viewBox="0 0 404 915" preserveAspectRatio="none" aria-hidden="true">
      <defs>
        <linearGradient id="coverDark" x1="0" y1="0" x2="1" y2="0">
          <stop offset="0" stop-color="#3a3a3a"/>
          <stop offset="1" stop-color="#5a5a5a"/>
        </linearGradient>
      </defs>
      <rect width="404" height="915" fill="url(#coverDark)"/>
      <rect width="404" height="14" fill="#4a4a4a"/>
      <polygon points="0,14 317,14 388,892 0,892" fill="var(--white)"/>
    </svg>
    <svg class="panel-bg" viewBox="0 0 404 915" preserveAspectRatio="none" role="img" aria-label="Photo of a power station with cooling tower and striped chimneys under a blue sky, with a glowing furnace interior inset">
      <defs>
        <linearGradient id="powerSky" x1="0" y1="0" x2="0" y2="1">
          <stop offset="0" stop-color="#7fa8d8"/>
          <stop offset="0.55" stop-color="#a9c4e2"/>
          <stop offset="0.8" stop-color="#c9c3b8"/>
          <stop offset="1" stop-color="#3f8a3a"/>
        </linearGradient>
      </defs>
      <polygon points="0,400 355,400 386,870 0,892" fill="url(#powerSky)"/>
    </svg>
    <svg class="panel-bg" viewBox="0 0 404 915" preserveAspectRatio="none" aria-hidden="true">
      <line x1="317" y1="14" x2="388" y2="892" stroke="var(--orange)" stroke-width="3"/>
      <line x1="0" y1="893" x2="388" y2="858" stroke="var(--orange)" stroke-width="3"/>
    </svg>
    <div class="cover-brand">KTR</div>
  </section>

</main>
</body>
</html>
```